Business Consultancy Wordpress Design

Small business analysis consultancy.

Looking for a bold, clean design for Wordpress. Final site will only be a few pages, some contact information, services provided and a little background information. Potentially a blog.

Colours to be as per logo, with either black or white as the main colour.

Link is www.halvicadvisory.com

More details to be included in the best few days

Name - Halvic Consulting
Provides - Project Consultancy
Updates

Project Deadline Extended
Reason: I am going to be on holiday with little access to the web over 28/02 - 05/03 and am therefore extending the deadline

Target Market(s)

Business professionals

Industry/Entity Type

Business

Colors

Designer to choose colors to be used in the design.

Requirements
Must have
• Must contain the logo in the header
Footer must fit a 3 column layout in wordpress

Business style, royalty free stock images
Nice to have
• Would like the 1 or 2 column wordpress style layout
Should not have
• must not be blog or magazine style layout or look and feel

```html
<!DOCTYPE html>
<html lang="en">
<head>
<meta charset="utf-8">
<title>Halvic Consulting</title>
<link href="https://fonts.googleapis.com/css2?family=Roboto:wght@300;400;500&display=swap" rel="stylesheet">
<style>
:root{
  --ink:#333;
  --muted:#555;
  --line:#e4e4e4;
  --accent-blue:#3aa0dd;
  --accent-green:#a6c11c;
  --logo-blue:#2d9ad6;
  --white:#fff;
  --hero-a:#4a4d50;
  --hero-b:#a9a9a7;
}
*{box-sizing:border-box;margin:0;padding:0}
html,body{width:1200px;height:613px;overflow:hidden;background:var(--white);font-family:'Roboto',sans-serif;color:var(--ink)}
.wrap{width:938px;margin-left:131px;position:relative}
.topbar{height:29px;border-bottom:1px solid var(--line)}
.topbar .wrap{display:flex;justify-content:space-between;height:29px}
.social{display:flex;border-left:1px solid var(--line)}
.social span{width:28px;height:29px;border-right:1px solid var(--line);display:flex;align-items:center;justify-content:center}
.social span i{width:8px;height:8px;border-radius:50%;background:#666;display:block}
.meta{display:flex;border-left:1px solid var(--line);font-size:12px;color:#555}
.meta div{padding:0 9px 0 12px;border-right:1px solid var(--line);display:flex;align-items:center;gap:6px}
.flag{width:16px;height:10px;background:#3b4a8c;display:inline-block}
.caret{font-size:9px}
.header{height:73px}
.header .wrap{display:flex;align-items:center;justify-content:space-between;height:73px}
.brand{display:flex;align-items:center;gap:10px}
.brand-dot{width:38px;height:38px;border-radius:50%;background:var(--logo-blue)}
.brand-name{font-size:24px;font-weight:400;color:#4a4a4a;letter-spacing:.5px;text-transform:uppercase;border-left:2px solid #4a4a4a;padding-left:8px;line-height:38px}
.nav{display:flex;align-items:center;gap:20px;font-size:13px;color:#444;position:relative}
.nav .active{color:var(--accent-blue)}
.badge{position:absolute;left:-23px;top:-18px;width:14px;height:14px;border-radius:50%;background:var(--accent-green);color:#fff;font-size:9px;text-align:center;line-height:14px}
.hero{height:401px;background:linear-gradient(100deg,var(--hero-a) 0%,#6b6c6c 45%,var(--hero-b) 75%,#d2d1cd 100%);position:relative}
.hero .wrap{padding-top:118px}
.hero h1{font-weight:300;font-size:42px;line-height:48px;color:var(--white);width:680px}
.hero p{font-weight:300;font-size:18px;color:#eee;margin-top:10px}
.btns{display:flex;gap:9px;margin-top:21px}
.btn{height:31px;padding:0 14px;border-radius:3px;color:#fff;font-size:13px;line-height:31px}
.btn.blue{background:var(--accent-blue)}
.btn.green{background:var(--accent-green)}
.dots{position:absolute;left:579px;top:372px;display:flex;gap:5px}
.dots i{width:7px;height:7px;border-radius:50%;background:rgba(255,255,255,.5)}
.dots i:first-child{background:#fff}
.features .wrap{display:flex;padding-top:40px}
.feature{display:flex;gap:18px;width:320px}
.feature h3{font-size:17px;font-weight:400;color:#333;margin-top:1px}
.feature p{font-size:12.5px;line-height:19px;color:var(--muted);margin-top:10px;width:245px}
</style>
</head>
<body>
<div class="topbar"><div class="wrap">
  <div class="social"><span><i></i></span><span><i></i></span><span><i></i></span><span><i></i></span><span><i></i></span></div>
  <div class="meta">
    <div>About Us <span class="caret">&#9662;</span></div>
    <div>Contact us: +555 210 48 316</div>
    <div><span class="flag"></span> English <span class="caret">&#9662;</span></div>
  </div>
</div></div>

<header class="header"><div class="wrap">
  <div class="brand"><span class="brand-dot"></span><span class="brand-name">Halvic Consulting</span></div>
  <nav class="nav">
    <span class="badge">!</span>
    <span class="active">Home &#8964;</span><span>About Us &#8964;</span><span>Elements &#8964;</span><span>Headers &#8964;</span><span>Portfolio &#8964;</span><span>Blog &#8964;</span>
    <svg width="13" height="13" viewBox="0 0 13 13"><circle cx="5.5" cy="5.5" r="4" fill="none" stroke="#333" stroke-width="2"/><line x1="8.5" y1="8.5" x2="12" y2="12" stroke="#333" stroke-width="2"/></svg>
    <svg width="12" height="10" viewBox="0 0 12 10" style="margin-left:8px"><rect y="0" width="12" height="2" fill="#333"/><rect y="4" width="12" height="2" fill="#333"/><rect y="8" width="12" height="2" fill="#333"/></svg>
  </nav>
</div></header>

<section class="hero" role="img" aria-label="Photo of a person seated at a desk facing a computer monitor in a bright office">
  <div class="wrap">
    <h1>Everything You Will Ever Need To Build an Amazing Website</h1>
    <p>Here's what we're working on and thinking.</p>
    <div class="btns"><span class="btn blue">View More</span><span class="btn green">View More</span></div>
  </div>
  <div class="dots"><i></i><i></i><i></i><i></i></div>
</section>

<section class="features"><div class="wrap">
  <div class="feature">
    <svg width="24" height="22" viewBox="0 0 24 22"><rect x="1" y="1" width="22" height="14" fill="none" stroke="#222" stroke-width="2"/><rect x="9" y="15" width="6" height="4" fill="#222"/><rect x="6" y="19" width="12" height="2" fill="#222"/></svg>
    <div><h3>Custom Shortcodes</h3><p>A wonderful serenity has taken possession of my entire soul, like these sweet mornings of spring</p></div>
  </div>
  <div class="feature">
    <svg width="20" height="22" viewBox="0 0 20 22"><path d="M10 1a7 7 0 0 0-4 12.7V16h8v-2.3A7 7 0 0 0 10 1z" fill="none" stroke="#222" stroke-width="2"/><rect x="6" y="17" width="8" height="2" fill="#222"/><rect x="8" y="20" width="4" height="2" fill="#222"/></svg>
    <div><h3>Visual Page Builder</h3><p>Pointing has no control about the blind texts it is an almost unorthographic life One day however a small</p></div>
  </div>
  <div class="feature">
    <svg width="24" height="22" viewBox="0 0 24 22"><path d="M3 15v-3a9 9 0 0 1 18 0v3" fill="none" stroke="#222" stroke-width="2.5"/><rect x="1" y="13" width="5" height="8" rx="1" fill="#222"/><rect x="18" y="13" width="5" height="8" rx="1" fill="#222"/></svg>
    <div><h3>Vector Icon Set</h3><p>When, while the lovely valley teems with vapour around me, and the meridian sun strikes the upper</p></div>
  </div>
</div></section>
</body>
</html>
```